Vorla constructions

We are predominantly a residential home builder based in Melbourne, Victoria Australia. We construct houses, apartments, townhouses, multi-unit developments.

The name of the company is "Vorla Constructions"
My company believes in building unique construction projects mainly residential homes. The target customers are upmarket Melbourne residents/investors.

I want the brand name "Vorla" to be part of the logo. There's no need to put the word construction in the logo at this stage.

I would also like some ideas for a slogan e.g. "Just build it." or "We build quality homes." But I would like something unique and different for a slogan not the same old cliche.

vorlaconstructions-example.com.au
e: mdelton@vorlaconstructions-example.com.au
M: 0417836519
Address: 8/3 Marlow Close Kelvale VIC 3197

Director:Mr Desmond Kellingworth

```html
<!DOCTYPE html>
<html lang="en">
<head>
<meta charset="utf-8">
<title>Vorla Constructions – Business Card</title>
<link rel="stylesheet" href="https://fonts.googleapis.com/css2?family=Lato:wght@300;400;700&display=swap">
<style>
  :root {
    --page-bg: #e4e4e6;
    --navy: #050538;
    --cyan: #1ab8e6;
    --white: #ffffff;
    --card-light: #f6f6f7;
    --card-shade: #dcdcdf;
    --ink: #111111;
  }
  * { margin: 0; padding: 0; box-sizing: border-box; }
  html, body {
    width: 1200px;
    height: 1000px;
    overflow: hidden;
    background: var(--page-bg);
    font-family: "Lato", sans-serif;
  }
  .business-card {
    position: absolute;
    left: 150px;
    top: 211px;
    width: 900px;
    height: 578px;
    background: linear-gradient(180deg, var(--card-light) 40%, var(--card-shade) 100%);
    overflow: hidden;
    box-shadow: 0 2px 6px rgba(0,0,0,0.18);
  }
  .card-band {
    position: absolute;
    inset: 0;
  }
  .brand-name {
    position: absolute;
    left: 44px;
    top: 52px;
    width: 330px;
    color: var(--white);
    font-weight: 400;
    white-space: nowrap;
  }
  .brand-name-main {
    display: block;
    font-size: 96px;
    line-height: 110px;
    letter-spacing: 2px;
  }
  .brand-name-sub {
    display: block;
    font-size: 36px;
    line-height: 44px;
    letter-spacing: 3px;
    margin-top: 6px;
  }
  .divider {
    position: absolute;
    left: 419px;
    top: 82px;
    height: 116px;
    border-left: 2px dotted rgba(255,255,255,0.75);
  }
  .slogan {
    position: absolute;
    left: 448px;
    top: 100px;
    font-size: 30px;
    font-weight: 300;
    line-height: 38px;
    color: var(--cyan);
    text-transform: uppercase;
    white-space: nowrap;
  }
  .holder {
    position: absolute;
    right: 32px;
    top: 252px;
    text-align: right;
    color: var(--ink);
  }
  .holder-name {
    font-size: 32px;
    font-weight: 300;
  }
  .holder-role {
    margin-top: 10px;
    font-size: 25px;
    font-weight: 700;
    letter-spacing: 0.5px;
  }
  .contact-list {
    position: absolute;
    left: 38px;
    top: 372px;
    list-style: none;
  }
  .contact-item {
    display: flex;
    align-items: center;
    height: 48px;
    font-size: 28px;
    font-weight: 300;
    color: var(--ink);
    white-space: nowrap;
  }
  .contact-icon {
    width: 40px;
    height: 36px;
    margin-right: 38px;
    flex: none;
  }
</style>
</head>
<body>
  <article class="business-card">
    <svg class="card-band" width="900" height="578" viewBox="0 0 900 578" aria-hidden="true">
      <path d="M0 0 H900 V215 C700 222 420 238 0 297 Z" fill="var(--navy)"/>
    </svg>

    <div class="brand-name">
      <span class="brand-name-main">Vorla</span>
      <span class="brand-name-sub">constructions</span>
    </div>
    <div class="divider"></div>
    <p class="slogan">Crafted<br>around your life</p>

    <div class="holder">
      <div class="holder-name">Mr Desmond Kellingworth</div>
      <div class="holder-role">DIRECTOR</div>
    </div>

    <ul class="contact-list">
      <li class="contact-item">
        <svg class="contact-icon" viewBox="0 0 40 36" aria-hidden="true">
          <path d="M20 2 C13 2 9 7 9 12 C9 20 20 34 20 34 C20 34 31 20 31 12 C31 7 27 2 20 2 Z" fill="var(--ink)"/>
          <circle cx="20" cy="12" r="4" fill="var(--card-light)"/>
        </svg>
        8/3 Marlow Close Kelvale VIC 3197
      </li>
      <li class="contact-item">
        <svg class="contact-icon" viewBox="0 0 40 36" aria-hidden="true">
          <rect x="11" y="1" width="18" height="34" rx="3" fill="var(--ink)"/>
          <rect x="14" y="6" width="12" height="21" fill="var(--card-light)"/>
          <circle cx="20" cy="31" r="1.8" fill="var(--card-light)"/>
        </svg>
        0417836519
      </li>
      <li class="contact-item">
        <svg class="contact-icon" viewBox="0 0 40 36" aria-hidden="true">
          <g fill="none" stroke="var(--ink)" stroke-width="2.4" stroke-linejoin="round">
            <path d="M3 14 L20 3 L37 14 V33 H3 Z"/>
            <path d="M3 14 L20 25 L37 14"/>
            <path d="M3 33 L16 22 M37 33 L24 22"/>
          </g>
        </svg>
        mdelton@vorlaconstructions-example.com.au
      </li>
      <li class="contact-item">
        <svg class="contact-icon" viewBox="0 0 40 36" aria-hidden="true">
          <g fill="none" stroke="var(--ink)" stroke-width="2.4" stroke-linejoin="round">
            <rect x="7" y="4" width="26" height="19"/>
            <path d="M7 23 L2 31 H38 L33 23"/>
          </g>
        </svg>
        vorlaconstructions-example.com.au
      </li>
    </ul>
  </article>
</body>
</html>
```